Geschäftspapiere für landwirtschaftlichen Betrieb
Zielgruppe
Landwirtschaftlicher Betrieb, Produktion und Vermarktung von hochwertigen Bio Produkten. Spezialisiert auf Ackerbau und den Anbau von Kartoffeln. Zielgruppe sind Menschen, die bewusst qualitativ hochwertige, nachhaltig produzierte Lebensmittel schätzen.
Aufgabenstellung
Das Design soll für einen Produktanhänger gestaltet werden. Die Produktanhänger werden auf Tragetaschen aus Papier aufgenäht. Je nach Inhalt (z.B. Kartoffeln, Äpfel, Zwiebel, Süsskartoffeln,...) wird der Produktname und die Details von uns selbst mittels Thermodruck aufgedruckt. Es wird also mittig Platz benötigt. Außerdem ist wichtig, dass durch das Zunähen der Säcke auf den oberen 3cm eine Naht die Etiketten durchkreuzen wird - bitte deshalb nicht das Firmenlogo zu weit oben platzieren.
Zur Etikettengröße: Breite 6cm, Höhe 16cm. (ca. 2mm Rand, dh 5,5cm und 15,5cm können bedruckt werden)
Inhalt: Unser Logo und Anschrift (Biohof Lindner, Mühlweg 27, 3468 Wiesenfeld, 02281/67914, www.biohoflindner-beispiel.at, AT-Landwirtschaft AT-BIO-718). Bitte mittig auch ausreichend Platz für die Produktbezeichnung lassen.
Das Design soll eher fein und elegant sein und sich nicht auf einen bestimmten Inhalt fokussieren (z.B. nur Kartoffeln abgebildet).
Im Anhang befinden sich Fotos von den derzeitigen Etiketten.
Wir wünschen uns eine deutliche überarbeitung oder komplette Neugestalltung der Etiketten.
Im Anhang ist noch eine PDF mit den neuen Kartoffelsäcken. Vielleicht ergibt sich dabei eine neue Idee :-)

```html
<!DOCTYPE html>
<html lang="de">
<head>
<meta charset="utf-8">
<title>Biohof Lindner – Produktanhänger</title>
<link href="https://fonts.googleapis.com/css2?family=Source+Sans+3:wght@300;400;700&display=swap" rel="stylesheet">
<style>
  :root {
    --brown: #63524d;
    --green: #c3c408;
    --white: #ffffff;
    --frame: #3a3a3a;
    --stage-top: #858585;
    --stage-bottom: #f8f8f8;
  }
  * { margin: 0; padding: 0; box-sizing: border-box; }
  html, body { width: 1200px; height: 2400px; overflow: hidden; }
  body { font-family: "Source Sans 3", "Myriad Pro", Arial, sans-serif; }

  .stage {
    position: absolute; left: 0; width: 1200px; height: 1200px;
    background: linear-gradient(to bottom, var(--stage-top) 0%, #dcdcdc 60%, var(--stage-bottom) 100%);
  }
  .stage--top { top: 0; }
  .stage--bottom { top: 1200px; }

  .tag {
    position: absolute; top: 101px; width: 374px; height: 997px;
    background: var(--white); border: 1px solid var(--frame);
    overflow: hidden;
  }
  .tag--left { left: 188px; }
  .tag--right { left: 638px; }

  .tag__print {
    position: absolute; inset: 3px; overflow: hidden;
  }
  .tag__fade {
    position: absolute; left: 0; right: 0; top: 390px; bottom: 0;
  }
  .tag__fade--green { background: linear-gradient(to bottom, rgba(195,196,8,0) 0%, rgba(195,196,8,.45) 40%, var(--green) 95%); }
  .tag__fade--brown { background: linear-gradient(to bottom, rgba(99,82,77,0) 0%, rgba(99,82,77,.5) 40%, var(--brown) 95%); }

  .tag__band { position: absolute; left: 0; top: 0; width: 368px; height: 991px; }

  .brand {
    position: absolute; top: 200px; left: 0; right: 0;
    display: flex; align-items: center; justify-content: center; gap: 10px;
    color: var(--brown); font-weight: 400; font-size: 30px; letter-spacing: .5px;
  }
  .brand__dot { width: 22px; height: 22px; border-radius: 50%; background: var(--green); flex: none; }

  .contact {
    position: absolute; right: 28px; top: 825px; text-align: right;
    font-size: 13.5px; line-height: 17px; font-weight: 300;
  }
  .contact--on-brown { color: var(--white); }
  .contact--on-green { color: var(--brown); }
  .contact strong { font-weight: 700; }
  .contact__block + .contact__block { margin-top: 19px; }
</style>
</head>
<body>

<section class="stage stage--top">
  <article class="tag tag--left">
    <div class="tag__print">
      <div class="brand"><span class="brand__dot"></span>Biohof Lindner</div>
      <svg class="tag__band" viewBox="0 0 368 991"><path d="M0,921 C70,860 220,800 368,793 L368,991 L0,991 Z" fill="var(--brown)"/></svg>
      <div class="contact contact--on-brown">
        <div class="contact__block"><strong>Biohof Lindner</strong><br>Mühlweg 27<br>3468 Wiesenfeld</div>
        <div class="contact__block"><strong>Telefon:</strong> 02281/67914<br><strong>Internet:</strong> www.biohoflindner-beispiel.at</div>
        <div class="contact__block">AT-Landwirtschaft | AT-BIO-718</div>
      </div>
    </div>
  </article>

  <article class="tag tag--right">
    <div class="tag__print">
      <div class="brand"><span class="brand__dot"></span>Biohof Lindner</div>
      <svg class="tag__band" viewBox="0 0 368 991"><path d="M0,921 C70,860 220,800 368,793 L368,991 L0,991 Z" fill="var(--green)"/></svg>
      <div class="contact contact--on-green">
        <div class="contact__block"><strong>Biohof Lindner</strong><br>Mühlweg 27<br>3468 Wiesenfeld</div>
        <div class="contact__block"><strong>Telefon:</strong> 02281/67914<br><strong>Internet:</strong> www.biohoflindner-beispiel.at</div>
        <div class="contact__block">AT-Landwirtschaft | AT-BIO-718</div>
      </div>
    </div>
  </article>
</section>

<section class="stage stage--bottom">
  <article class="tag tag--left">
    <div class="tag__print">
      <div class="tag__fade tag__fade--green"></div>
      <div class="brand"><span class="brand__dot"></span>Biohof Lindner</div>
      <svg class="tag__band" viewBox="0 0 368 991"><path d="M0,921 C70,860 220,800 368,793 L368,991 L0,991 Z" fill="var(--brown)"/></svg>
      <div class="contact contact--on-brown">
        <div class="contact__block"><strong>Biohof Lindner</strong><br>Mühlweg 27<br>3468 Wiesenfeld</div>
        <div class="contact__block"><strong>Telefon:</strong> 02281/67914<br><strong>Internet:</strong> www.biohoflindner-beispiel.at</div>
        <div class="contact__block">AT-Landwirtschaft | AT-BIO-718</div>
      </div>
    </div>
  </article>

  <article class="tag tag--right">
    <div class="tag__print">
      <div class="tag__fade tag__fade--brown"></div>
      <div class="brand"><span class="brand__dot"></span>Biohof Lindner</div>
      <svg class="tag__band" viewBox="0 0 368 991"><path d="M0,921 C70,860 220,800 368,793 L368,991 L0,991 Z" fill="var(--green)"/></svg>
      <div class="contact contact--on-green">
        <div class="contact__block"><strong>Biohof Lindner</strong><br>Mühlweg 27<br>3468 Wiesenfeld</div>
        <div class="contact__block"><strong>Telefon:</strong> 02281/67914<br><strong>Internet:</strong> www.biohoflindner-beispiel.at</div>
        <div class="contact__block">AT-Landwirtschaft | AT-BIO-718</div>
      </div>
    </div>
  </article>
</section>

</body>
</html>
```